K & R Acreage Works. Business card design

We need a business card designed for a new business. We have a bulldozer and tractor service. We clear land and make wildlife food plots. We provide disking, bush hogging, and site prep services.
I have attached an image of a business card that I like and would like my business cards to look similar.

Target Market(s)

anyone needing bulldozer and/or tractor services

Industry/Entity Type

Business

Contact Information for Business Card

K & R Acreage Works, Operated by 7-M-Ranch
Doug Pelham
601-473-5826
dpr4178@mailvexo.com

Font styles to use
Sans Serif

Colors

Designer to choose colors to be used in the design.

Requirements
Must have
• image of tractor and bulldozer
• Land Clearing
• Wildlife food plots
• Bush Hogging
• Disking
• Site prep
Nice to have
• i have included a image of a business card that i like. I would like mine to be similar.

```html
<!DOCTYPE html>
<html lang="en">
<head>
<meta charset="utf-8">
<title>K &amp; R Acreage Works – Business Card</title>
<link href="https://fonts.googleapis.com/css2?family=Bebas+Neue&family=Roboto:wght@400&display=swap" rel="stylesheet">
<style>
  :root {
    --backdrop: #141414;
    --panel: #1b1b1b;
    --ink: #ffffff;
    --divider-light: #f2f2f2;
    --divider-dark: #9a9a9a;
    --gap: #ffffff;
    --foliage: #5f7d3a;
    --foliage-deep: #3e5a26;
    --soil: #8a7458;
    --machine-yellow: #c9a52a;
    --machine-orange: #c9542c;
    --sky: #b9cde0;
  }
  html, body {
    margin: 0;
    width: 1200px;
    height: 897px;
    overflow: hidden;
    background: var(--backdrop);
  }
  .card {
    position: absolute;
    left: 100px;
    top: 164px;
    width: 1000px;
    height: 569px;
    display: flex;
    background: var(--panel);
    box-shadow: 0 8px 30px rgba(0,0,0,.6);
  }
  .card__info {
    width: 497px;
    position: relative;
    color: var(--ink);
  }
  .card__company {
    position: absolute;
    left: 34px;
    top: 38px;
    margin: 0;
    font-family: "Bebas Neue", sans-serif;
    font-weight: 400;
    font-size: 46px;
    line-height: 48px;
    letter-spacing: 0.5px;
  }
  .card__name {
    position: absolute;
    left: 37px;
    top: 204px;
    margin: 0;
    font-family: "Roboto", sans-serif;
    font-weight: 400;
    font-size: 33px;
  }
  .card__contact {
    position: absolute;
    left: 38px;
    top: 268px;
    margin: 0;
    font-family: "Roboto", sans-serif;
    font-size: 30px;
    line-height: 40px;
  }
  .card__services {
    position: absolute;
    left: 38px;
    top: 373px;
    margin: 0;
    padding: 0;
    list-style: none;
    font-family: "Roboto", sans-serif;
    font-size: 30px;
    line-height: 40px;
  }
  .card__services li {
    position: relative;
    padding-left: 42px;
  }
  .card__services li::before {
    content: "";
    position: absolute;
    left: 4px;
    top: 15px;
    width: 11px;
    height: 11px;
    border-radius: 50%;
    background: var(--ink);
  }
  .card__divider {
    width: 12px;
    background: linear-gradient(90deg, var(--divider-light), var(--divider-dark));
  }
  .card__gallery {
    flex: 1;
    display: flex;
    flex-direction: column;
    gap: 5px;
    background: var(--gap);
  }
  .photo { display: block; }
  .photo--main {
    height: 405px;
    background: linear-gradient(180deg, var(--foliage) 0%, var(--foliage-deep) 45%, var(--machine-yellow) 60%, var(--soil) 100%);
  }
  .card__thumbs {
    flex: 1;
    display: flex;
    gap: 5px;
  }
  .photo--thumb { flex: 1; }
  .photo--dozer-small {
    background: linear-gradient(180deg, var(--sky) 0%, var(--machine-yellow) 45%, var(--soil) 100%);
  }
  .photo--tractor {
    background: linear-gradient(180deg, var(--foliage) 0%, var(--machine-orange) 50%, var(--soil) 100%);
  }
  .photo--dozer-work {
    background: linear-gradient(180deg, var(--foliage-deep) 0%, var(--machine-yellow) 50%, #4a3d2e 100%);
  }
</style>
</head>
<body>
  <div class="card">
    <section class="card__info">
      <h1 class="card__company">K &amp; R Acreage Works<br>Operated by 7-M-Ranch</h1>
      <p class="card__name">DOUG PELHAM</p>
      <p class="card__contact">P : 601-473-5826<br>E : dpr4178@mailvexo.com</p>
      <ul class="card__services">
        <li>Land Clearing</li>
        <li>Wildlife food plots</li>
        <li>Bush Hogging</li>
        <li>Disking | Site prep</li>
      </ul>
    </section>
    <div class="card__divider"></div>
    <section class="card__gallery">
      <div class="photo photo--main" role="img" aria-label="Yellow bulldozer with blade lowered in front of green trees"></div>
      <div class="card__thumbs">
        <div class="photo photo--thumb photo--dozer-small" role="img" aria-label="Yellow bulldozer pushing dirt"></div>
        <div class="photo photo--thumb photo--tractor" role="img" aria-label="Orange tractor with front loader in a field"></div>
        <div class="photo photo--thumb photo--dozer-work" role="img" aria-label="Bulldozer grading a pile of dark soil"></div>
      </div>
    </section>
  </div>
</body>
</html>
```